BQL Groundworks & Freight Business Card

Can you please design a business card for an Earthworks, Haulage truck and machinery hire company. They also provide sand soil and mulch supply, as well as screening of products. Can you re-create the logo from the attached but add BQL Groundworks & Freight just use the three diamond design.

Target Market(s)

Earthmoving and Transport, Landscapers, Construction

Contact Information for Business Card

ABN 52 907 334 816, Doug Pelham, Managing Director, BQL Groundworks & Freight Mobile 0438 256 904 Email bqlfreight2010@mailvane.net

Font styles to use
Sans Serif

Colors
ec1f27
000000
cbcbcb
ffffff

Requirements
Must have
• Listed on the back, Earthworks | Haulage | Truck and Machinery Hire | Sand, Soil & Mulch Supply | Screening of Products
Nice to have
• Would be good for it to look appealing to a mans man, because it relates to heavy machinery, earthworks, construction etc. Black, red and white would be good maybe with a bit of silver somewhere.
Should not have
• not sure

```html
<!DOCTYPE html>
<html lang="en">
<head>
<meta charset="utf-8">
<title>BQL Groundworks &amp; Freight – Business Card</title>
<link href="https://fonts.googleapis.com/css2?family=Lato:wght@400;700;900&display=swap" rel="stylesheet">
<style>
  :root {
    --red: #ec1f27;
    --black: #000000;
    --silver: #cbcbcb;
    --white: #ffffff;
    --backdrop-light: #c4c4c4;
    --backdrop-dark: #8e8e8e;
  }
  * { margin: 0; padding: 0; box-sizing: border-box; }
  html, body { width: 1200px; height: 1200px; overflow: hidden; }
  body {
    background: radial-gradient(ellipse at 40% 35%, var(--backdrop-light), var(--backdrop-dark));
    font-family: "Lato", Arial, sans-serif;
    position: relative;
  }
  .card {
    position: absolute;
    left: 150px;
    width: 900px;
    height: 514px;
    background: var(--white);
    border-radius: 26px;
    overflow: hidden;
    box-shadow: 0 18px 40px rgba(0,0,0,0.28);
  }
  .card--back { top: 70px; }
  .card--front { top: 630px; }

  /* Back side */
  .card--back .brand {
    position: absolute;
    top: 170px; left: 0; right: 0;
    display: flex; align-items: center; justify-content: center; gap: 22px;
  }
  .brand-square {
    width: 58px; height: 58px;
    background: var(--black);
  }
  .brand-name {
    color: var(--red);
    font-weight: 700;
    text-transform: uppercase;
    letter-spacing: 1px;
  }
  .card--back .brand-name { font-size: 40px; }
  .services {
    position: absolute;
    left: 0; right: 0; top: 370px;
    text-align: center;
    color: var(--black);
    font-size: 22px;
    line-height: 1.4;
  }
  .card--back .base-strip {
    position: absolute; left: 0; right: 0; bottom: 0;
    height: 14px; background: var(--red);
  }

  /* Front side */
  .card--front .brand {
    position: absolute;
    top: 70px; right: 60px;
    display: flex; align-items: center; gap: 14px;
  }
  .card--front .brand-square { width: 36px; height: 36px; }
  .card--front .brand-name { font-size: 22px; }
  .person {
    position: absolute; left: 70px; top: 200px;
  }
  .person-name {
    font-size: 46px; font-weight: 900; color: var(--black);
    text-transform: uppercase; letter-spacing: -0.5px;
  }
  .person-role {
    font-size: 24px; color: var(--red);
    text-transform: uppercase; letter-spacing: 0.5px;
  }
  .silver-rule {
    position: absolute; left: 0; right: 0; top: 330px;
    height: 10px; background: var(--silver);
  }
  .contact-band {
    position: absolute; left: 0; right: 0; top: 346px; bottom: 0;
    background: var(--red);
    color: var(--white);
    padding: 22px 0 0 90px;
    font-size: 22px;
    line-height: 1.3;
  }
  .contact-band .company { margin-bottom: 14px; }
  .contact-line { display: flex; align-items: center; gap: 14px; }
  .contact-line svg { width: 18px; height: 18px; fill: var(--white); flex: none; }
</style>
</head>
<body>

<section class="card card--back">
  <div class="brand">
    <span class="brand-square"></span>
    <span class="brand-name">BQL Groundworks &amp; Freight</span>
  </div>
  <p class="services">
    Earthworks | Haulage<br>
    Truck and Machinery Hire | Sand, Soil &amp; Mulch Supply | Screening of Products
  </p>
  <div class="base-strip"></div>
</section>

<section class="card card--front">
  <div class="brand">
    <span class="brand-square"></span>
    <span class="brand-name">BQL Groundworks &amp; Freight</span>
  </div>
  <div class="person">
    <h1 class="person-name">Doug Pelham</h1>
    <p class="person-role">Managing Director</p>
  </div>
  <div class="silver-rule"></div>
  <div class="contact-band">
    <div class="company">
      ABN 52 907 334 816<br>
      BQL Groundworks &amp; Freight
    </div>
    <div class="contact-line">
      <svg viewBox="0 0 24 24" aria-hidden="true"><path d="M6.6 10.8a15 15 0 0 0 6.6 6.6l2.2-2.2a1 1 0 0 1 1-.25 11.4 11.4 0 0 0 3.6.57 1 1 0 0 1 1 1V20a1 1 0 0 1-1 1A17 17 0 0 1 3 4a1 1 0 0 1 1-1h3.5a1 1 0 0 1 1 1c0 1.25.2 2.45.57 3.6a1 1 0 0 1-.25 1z"/></svg>
      <span>0438 256 904</span>
    </div>
    <div class="contact-line">
      <svg viewBox="0 0 24 24" aria-hidden="true"><path d="M2 5h20v14H2z M2 5l10 8 10-8" fill="none" stroke="#fff" stroke-width="2"/></svg>
      <span>bqlfreight2010@mailvane.net</span>
    </div>
  </div>
</section>

</body>
</html>
```